Copper lark buildworks

Copper lark buildworks is a small construction company.
Who is a licenced builder, Carpenter, joiner,
working on heritage ,new build, speacial projects and sometimes furniture

Industry/Entity Type

Construction

```html
<!DOCTYPE html>
<html lang="en">
<head>
<meta charset="utf-8">
<title>Copper lark buildworks – Business Card</title>
<link rel="stylesheet" href="https://fonts.googleapis.com/css2?family=Open+Sans:wght@400;600&family=Roboto+Slab:wght@500&display=swap">
<style>
  :root {
    --page-bg: #e9e9e7;
    --brand-green: #12a602;
    --charcoal: #333333;
    --disc-white: #f1f1f0;
    --text-light: #ffffff;
    --text-dark: #2e2e2e;
  }
  * { box-sizing: border-box; margin: 0; padding: 0; }
  html, body {
    width: 1200px;
    height: 900px;
    overflow: hidden;
    background: var(--page-bg);
  }
  .business-card {
    position: absolute;
    left: 120px;
    top: 152px;
    width: 960px;
    height: 595px;
    background: var(--brand-green);
    overflow: hidden;
    box-shadow: 0 10px 30px rgba(0,0,0,0.18);
  }
  .dark-band {
    position: absolute;
    top: 0;
    right: 0;
    width: 302px;
    height: 100%;
    background: var(--charcoal);
  }
  .brand-disc {
    position: absolute;
    left: 398px;
    top: 40px;
    width: 514px;
    height: 514px;
    border-radius: 50%;
    background: radial-gradient(circle at 45% 40%, #ffffff 0%, var(--disc-white) 60%, #e2e2e1 100%);
    display: flex;
    align-items: center;
    justify-content: center;
  }
  .brand-name {
    font-family: "Roboto Slab", Georgia, serif;
    font-weight: 500;
    font-size: 34px;
    color: var(--text-dark);
    letter-spacing: 0.3px;
  }
  .person {
    position: absolute;
    left: 58px;
    top: 62px;
    color: var(--text-light);
  }
  .person-name {
    font-family: "Roboto Slab", Georgia, serif;
    font-weight: 500;
    font-size: 40px;
    line-height: 1.2;
  }
  .person-role {
    font-family: "Open Sans", Arial, sans-serif;
    font-size: 24px;
    margin-top: 6px;
    margin-left: 3px;
  }
  .contact-list {
    position: absolute;
    left: 58px;
    top: 290px;
    list-style: none;
    font-family: "Open Sans", Arial, sans-serif;
    font-size: 24px;
    color: var(--text-light);
  }
  .contact-list li {
    display: flex;
    align-items: center;
    height: 35px;
  }
  .contact-icon {
    width: 20px;
    height: 20px;
    margin-right: 13px;
    fill: var(--text-light);
  }
  .address {
    position: absolute;
    left: 60px;
    top: 462px;
    font-family: "Open Sans", Arial, sans-serif;
    font-size: 24px;
    line-height: 35px;
    color: var(--text-light);
    font-style: normal;
  }
</style>
</head>
<body>
  <article class="business-card">
    <div class="dark-band"></div>
    <div class="brand-disc">
      <span class="brand-name">Copper lark buildworks</span>
    </div>

    <header class="person">
      <h1 class="person-name">Daniel Hartley</h1>
      <p class="person-role">Managing Director</p>
    </header>

    <ul class="contact-list">
      <li>
        <svg class="contact-icon" viewBox="0 0 20 20" aria-hidden="true"><path d="M6 1h8a1.5 1.5 0 0 1 1.5 1.5v15A1.5 1.5 0 0 1 14 19H6a1.5 1.5 0 0 1-1.5-1.5v-15A1.5 1.5 0 0 1 6 1zm.5 2.5v11h7v-11zM10 15.6a1 1 0 1 0 0 2 1 1 0 0 0 0-2z"/></svg>
        <span>055-210 384 617</span>
      </li>
      <li>
        <svg class="contact-icon" viewBox="0 0 20 20" aria-hidden="true"><path d="M1 6c0-2 4-3.5 9-3.5S19 4 19 6v1.5h-4.5V6c0-.8-2-1.2-4.5-1.2S5.5 5.2 5.5 6v1.5H1zM5 9h10l3 7.5H2zm5 1.6a2.4 2.4 0 1 0 0 4.8 2.4 2.4 0 0 0 0-4.8z"/></svg>
        <span>055-210 384 617</span>
      </li>
      <li>
        <svg class="contact-icon" viewBox="0 0 20 20" aria-hidden="true"><path d="M2 4h16v1.2L10 11 2 5.2zm0 3l8 5.8L18 7v9H2z"/></svg>
        <span>hello@copperlark.com</span>
      </li>
      <li>
        <svg class="contact-icon" viewBox="0 0 20 20" aria-hidden="true"><path d="M10 1a9 9 0 1 0 0 18 9 9 0 0 0 0-18zm-1 3.2c.8.6 1 1.6.2 2.3-.9.7-2.2.5-2.6 1.6-.4 1 .6 1.9 1.6 2.1 1.3.3 2 1.2 1.7 2.5-.2 1 .4 2.2.8 3.1A6.6 6.6 0 0 1 4.2 7.2 6.6 6.6 0 0 1 9 4.2zm3.5.6a6.6 6.6 0 0 1 3.8 7.5c-.7-.6-1.5-1.4-1.3-2.5.2-1.2-1-1.7-1.8-2.4-.8-.7-.9-1.7-.7-2.6z"/></svg>
        <span>www.copperlark.com</span>
      </li>
    </ul>

    <address class="address">
      48 Ashgrove Lane, Kelmore<br>
      Northfield, 204519.
    </address>
  </article>
</body>
</html>
```